New brand for digital company - your chance to get creative

We need to create a brand for our new business 'Lanternfish Digital'. Please read the brief below before progressing as we are looking for some quite specific outputs.

Background

We are positioning ourselves as ‘marketing technologists’ - we're helping businesses engage with their customers in the online space.

Our tactics include branding, marketing, online management, and social media, however we are differentiating ourselves by focusing on overall strategy, not just tactics. Our tagline is ‘Online made simple’.

We have stipulated some parameters for the brand but otherwise want designers to exercise their creativity.

Requirements
Must have
• We want to see an entire concept, not just a logo.

```html
<!DOCTYPE html>
<html lang="en">
<head>
<meta charset="utf-8">
<title>Lanternfish Digital</title>
<link rel="stylesheet" href="https://fonts.googleapis.com/css2?family=Open+Sans:wght@400;600&display=swap">
<style>
  :root {
    --header-white: #ffffff;
    --brand-ink: #163a25;
    --brand-square: #9a928c;
    --accent-pink: #e4004f;
    --panel-fill: rgba(215, 212, 208, 0.62);
    --tab-fill: rgba(120, 112, 106, 0.55);
    --tab-active: rgba(215, 212, 208, 0.62);
    --text-dark: #163a25;
    --stripe-light: rgba(235, 232, 228, 0.7);
    --stripe-dark: rgba(40, 36, 34, 0.75);
    --icon-a: #2a9fd0;
    --icon-b: #ef7a22;
    --icon-c: #4a67a8;
  }
  * { margin: 0; padding: 0; box-sizing: border-box; }
  html, body { width: 1200px; height: 900px; overflow: hidden; }
  body { position: relative; font-family: "Open Sans", Arial, sans-serif; }

  .office-photo {
    position: absolute; inset: 0;
    background:
      radial-gradient(ellipse 30% 40% at 12% 50%, rgba(200, 215, 210, 0.55), transparent 70%),
      radial-gradient(ellipse 35% 45% at 85% 55%, rgba(120, 60, 40, 0.6), transparent 75%),
      linear-gradient(180deg, #5a4d42 0%, #4a3a30 40%, #2e2420 75%, #1e1816 100%);
  }

  .site-header {
    position: absolute; left: 0; top: 58px; width: 1200px; height: 200px;
    background: var(--header-white);
  }
  .brand {
    position: absolute; left: 40px; top: 0; height: 200px;
    display: flex; align-items: center; gap: 20px;
  }
  .brand-square {
    width: 44px; height: 44px;
    background: var(--brand-square);
  }
  .brand-name {
    font-family: "Open Sans", Arial, sans-serif; font-weight: 600;
    font-size: 44px; line-height: 1;
    color: var(--brand-ink);
  }
  .social-links {
    position: absolute; right: 32px; top: 44px;
    display: flex; gap: 17px; list-style: none;
  }
  .social-links li {
    width: 100px; height: 100px; border-radius: 18px;
  }
  .social-links .link-a { background: var(--icon-a); }
  .social-links .link-b { background: var(--icon-b); }
  .social-links .link-c { background: var(--icon-c); }

  .tabs {
    position: absolute; left: 185px; top: 317px;
    display: flex; gap: 4px; list-style: none;
  }
  .tabs li {
    width: 108px; height: 39px;
    background: var(--tab-fill);
    font-size: 13px; font-weight: 600; line-height: 39px; text-align: center;
    color: var(--text-dark); text-transform: uppercase;
  }
  .tabs .is-active { background: var(--tab-active); color: var(--accent-pink); padding-right: 12px; }

  .content-panel {
    position: absolute; left: 185px; top: 356px; width: 588px; height: 544px;
    background: var(--panel-fill);
    padding: 54px 50px 0 50px;
  }
  .content-panel p {
    font-size: 13.4px; line-height: 37.6px; letter-spacing: 0.3px;
    text-transform: uppercase;
    text-align: justify; color: var(--text-dark);
    margin-bottom: 37.6px;
  }

  .side-stripes { position: absolute; left: 786px; top: 356px; width: 59px; height: 544px; display: flex; }
  .side-stripes span { display: block; height: 100%; }
  .side-stripes .light { width: 20px; background: var(--stripe-light); }
  .side-stripes .dark { width: 19px; background: var(--stripe-dark); }
</style>
</head>
<body>
  <div class="office-photo" role="img" aria-label="Blurred photograph of a bright open-plan office with a person walking, desks and a bicycle"></div>

  <header class="site-header">
    <div class="brand">
      <span class="brand-square"></span>
      <span class="brand-name">Lanternfish Digital</span>
    </div>
    <ul class="social-links" aria-label="Social links">
      <li class="link-a"></li>
      <li class="link-b"></li>
      <li class="link-c"></li>
    </ul>
  </header>

  <ul class="tabs">
    <li class="is-active">Lorem</li>
    <li>Ipsum</li>
    <li>Amet</li>
    <li>Enipm</li>
  </ul>

  <main class="content-panel">
    <p>Lorem ipsum dolor sit amet, consectetur adipiscing elit. Quisque pharetra, ante ac accumsan tincidunt, ligula orci laoreet est, non hendrerit enim tellus a lacus. Nam euismod porta leo a adipiscing. Nullam eget lacus a dui dapibus condimentum. Sed at bibendum est. In ac dolor et ligula scelerisque suscipit vel sed tortor. Morbi ac orci lectus, non mattis diam. Nam lacinia cursus lorem vel fermentum. Duis pulvinar, dolor et convallis egestas, arcu lacus aliquam enim, vel tincidunt orci justo at dui.</p>
    <p>Suspendisse convallis magna scelerisque est gravida posuere. Phasellus lacinia ornare ultrices. Nam vitae mauris massa. Etiam sapien sapien, dictum in pharetra vel, placerat eget augue. Lorem ipsum dolor sit amet, consectetur adipiscing elit. Nullam iaculis, nisi vitae tempor luctus, magna erat rutrum velit.</p>
  </main>

  <div class="side-stripes" aria-hidden="true">
    <span class="light"></span><span class="dark"></span><span class="light"></span>
  </div>
</body>
</html>
```